BRV TAX & ACCOUNTING business card
Income tax, audit, bookkeeping, setup, training and services
Professional
Derek Lim Varga
48 Bexwell Drive
Toronto, ON M2K 4T8
brv_tax@quillmail.ca

```html
<!DOCTYPE html>
<html lang="en">
<head>
<meta charset="utf-8">
<title>BRV Tax &amp; Accounting – Business Card</title>
<link rel="stylesheet" href="https://fonts.googleapis.com/css2?family=Montserrat:wght@800&family=Open+Sans:wght@400;600&display=swap">
<style>
  :root {
    --brand-green: #7cc122;
    --brand-dark: #1c1c1c;
    --card-white: #ffffff;
    --card-shade: #ececec;
    --backdrop: #d9dadb;
    --text-grey: #3a3a3a;
  }
  * { margin: 0; padding: 0; box-sizing: border-box; }
  html, body { width: 1200px; height: 864px; overflow: hidden; }
  body {
    background: var(--backdrop);
    display: flex;
    flex-direction: column;
    align-items: center;
    justify-content: center;
    gap: 56px;
    font-family: "Open Sans", Arial, sans-serif;
  }
  .card {
    position: relative;
    width: 600px;
    height: 345px;
    border-radius: 22px;
    background: linear-gradient(160deg, var(--card-white) 55%, var(--card-shade));
    box-shadow: 0 10px 26px rgba(0,0,0,.22);
    overflow: hidden;
  }
  .brand-name {
    font-family: "Montserrat", Arial, sans-serif;
    font-weight: 800;
    color: var(--brand-green);
    line-height: 1;
    text-align: center;
  }
  .brand-name .brand-word { display: block; font-size: 74px; letter-spacing: 2px; }
  .brand-name .brand-trade { display: block; font-size: 17px; letter-spacing: 1px; margin-top: 6px; }

  /* front */
  .card-front { display: flex; align-items: center; justify-content: center; }

  /* back */
  .card-back .swoosh { position: absolute; inset: 0; width: 100%; height: 100%; }
  .card-back .brand-block { position: absolute; left: 58px; top: 68px; }
  .card-back .brand-name .brand-word { font-size: 62px; }
  .card-back .brand-name .brand-trade { font-size: 14px; }
  .holder-name {
    margin-top: 20px;
    font-size: 17px;
    font-weight: 600;
    color: var(--brand-green);
    text-align: center;
  }
  .contact-list {
    position: absolute;
    right: 34px;
    top: 56px;
    list-style: none;
    font-size: 13px;
    color: var(--text-grey);
  }
  .contact-list li { display: flex; align-items: center; gap: 9px; height: 24px; }
  .contact-list li.continued { padding-left: 27px; margin-top: -4px; }
  .contact-icon { width: 18px; height: 18px; flex: none; }
</style>
</head>
<body>

<section class="card card-front" aria-label="Card front">
  <p class="brand-name"><span class="brand-word">BRV</span><span class="brand-trade">TAX &amp; ACCOUNTING</span></p>
</section>

<section class="card card-back" aria-label="Card back">
  <svg class="swoosh" viewBox="0 0 600 345" preserveAspectRatio="none" aria-hidden="true">
    <path d="M0 205 Q 170 325 600 322 L600 345 L0 345 Z" fill="var(--brand-green)"/>
    <path d="M0 188 Q 190 300 540 312 Q 200 318 0 222 Z" fill="var(--brand-dark)"/>
  </svg>

  <div class="brand-block">
    <p class="brand-name"><span class="brand-word">BRV</span><span class="brand-trade">TAX &amp; ACCOUNTING</span></p>
    <p class="holder-name">Derek Lim Varga</p>
  </div>

  <ul class="contact-list">
    <li>
      <svg class="contact-icon" viewBox="0 0 18 18" aria-hidden="true"><circle cx="9" cy="9" r="9" fill="var(--brand-green)"/><path d="M9 4a3 3 0 0 0-3 3c0 2.3 3 6 3 6s3-3.7 3-6a3 3 0 0 0-3-3z" fill="#fff"/><circle cx="9" cy="7" r="1.1" fill="var(--brand-green)"/></svg>
      48 Bexwell Drive
    </li>
    <li class="continued">Toronto, ON M2K 4T8</li>
    <li>
      <svg class="contact-icon" viewBox="0 0 18 18" aria-hidden="true"><circle cx="9" cy="9" r="9" fill="var(--brand-green)"/><path d="M6 4.5l1.8 0 .8 2.4-1.1.9a6 6 0 0 0 2.7 2.7l.9-1.1 2.4.8 0 1.8c0 .5-.4.9-.9.9A7.6 7.6 0 0 1 5.1 5.4c0-.5.4-.9.9-.9z" fill="#fff"/></svg>
      416-555-0193
    </li>
    <li>
      <svg class="contact-icon" viewBox="0 0 18 18" aria-hidden="true"><circle cx="9" cy="9" r="9" fill="var(--brand-green)"/><rect x="4.5" y="6" width="9" height="6.4" rx=".8" fill="#fff"/><path d="M4.8 6.4 9 9.6l4.2-3.2" fill="none" stroke="var(--brand-green)" stroke-width="1"/></svg>
      brv_tax@quillmail.ca
    </li>
    <li>
      <svg class="contact-icon" viewBox="0 0 18 18" aria-hidden="true"><circle cx="9" cy="9" r="9" fill="var(--brand-green)"/><circle cx="9" cy="9" r="4.6" fill="none" stroke="#fff" stroke-width="1.1"/><path d="M4.4 9h9.2M9 4.4c-2 2.6-2 6.6 0 9.2M9 4.4c2 2.6 2 6.6 0 9.2" fill="none" stroke="#fff" stroke-width="1"/></svg>
      www.brvtaxgroup.ca
    </li>
  </ul>
</section>

</body>
</html>
```